Design business cards for Vantrelo

I am looking for a clean, crisp and professional business card design. A logo already exists with which to work, which is attached in various formats. The design needs to be print ready. A clear brief is attached - please read it carefully and ensure you can deliver what is required. Looking forward to awarding the prize to a great design and great designer!

```html
<!DOCTYPE html>
<html lang="en">
<head>
<meta charset="utf-8">
<title>Vantrelo Business Cards</title>
<link href="https://fonts.googleapis.com/css2?family=Open+Sans:wght@400;700&display=swap" rel="stylesheet">
<style>
  :root{
    --bg:#e6e4e0;
    --card:#fbfbfb;
    --ink:#2e2e2e;
    --muted:#8a8a8a;
    --text:#4a4a4a;
    --accent:#6e2a6f;
    --deco:#ececec;
  }
  *{margin:0;padding:0;box-sizing:border-box}
  html,body{width:1200px;height:1003px;overflow:hidden;background:var(--bg);font-family:"Open Sans",Arial,sans-serif}
  .sheet{position:relative;width:1200px;height:1003px}
  .card{position:absolute;left:215px;width:770px;height:440px;background:var(--card);box-shadow:0 4px 14px rgba(0,0,0,.12);overflow:hidden}
  .card--back{top:50px}
  .card--front{top:513px}
  .deco{position:absolute;border-radius:50%;background:var(--deco)}
  .card--back .deco{width:260px;height:260px;left:-60px;top:-90px}
  .card--front .deco{width:260px;height:260px;right:-40px;top:-100px}
  .brand{position:absolute;display:flex;align-items:center;gap:16px}
  .brand__dot{width:44px;height:44px;border-radius:50%;background:var(--accent)}
  .brand__name{font-size:46px;font-weight:400;color:var(--ink);letter-spacing:.5px}
  .card--back .brand{left:120px;top:232px}
  .card--front .brand{left:50px;top:50px}
  .website{position:absolute;right:50px;top:58px;font-size:17px;color:var(--text)}
  .person{position:absolute;left:50px;top:150px}
  .person__name{font-size:24px;font-weight:700;color:var(--accent)}
  .person__cred{font-size:15px;font-weight:400;color:var(--muted);margin-left:4px}
  .person__role{font-size:17px;color:var(--muted);margin-top:2px}
  .address{position:absolute;left:50px;top:238px;font-size:17px;line-height:1.4;color:var(--text)}
  .contacts{position:absolute;list-style:none;font-size:17px;color:var(--text)}
  .contacts li{display:flex;align-items:center;gap:12px;height:30px}
  .contacts svg{width:18px;height:18px;fill:var(--accent)}
  .contacts--left{left:50px;top:318px}
  .contacts--right{left:430px;top:318px}
  .marker{width:18px;height:18px;border-radius:50%;background:var(--accent);flex:none}
</style>
</head>
<body>
<main class="sheet">
  <section class="card card--back">
    <div class="deco"></div>
    <div class="brand">
      <span class="brand__dot"></span>
      <span class="brand__name">Vantrelo</span>
    </div>
    <p class="website">www.vantrelo.com.au</p>
  </section>

  <section class="card card--front">
    <div class="deco"></div>
    <div class="brand">
      <span class="brand__dot"></span>
      <span class="brand__name">Vantrelo</span>
    </div>
    <div class="person">
      <p><span class="person__name">Daniel Marsh</span><span class="person__cred">BE(Hons) PhD MIEAust GAICD</span></p>
      <p class="person__role">Director, Principal Consultant</p>
    </div>
    <p class="address">42 Ashby Lane, Kelmore East<br>Victoria 3190 Australia</p>
    <ul class="contacts contacts--left">
      <li><svg viewBox="0 0 18 18"><rect x="4" y="1" width="10" height="16" rx="2"/><rect x="6" y="3" width="6" height="9" fill="#fbfbfb"/></svg>+61 (0)400 555 01</li>
      <li><svg viewBox="0 0 18 18"><rect x="1" y="4" width="16" height="11" rx="1"/><path d="M1.5 4.5 9 10.5 16.5 4.5" fill="none" stroke="#fbfbfb" stroke-width="1.5"/></svg>dmarsh@vantrelo.com.au</li>
    </ul>
    <ul class="contacts contacts--right">
      <li><span class="marker"></span>dan.marsh22</li>
      <li><span class="marker"></span>au.profilehub.net/in/dmarsh</li>
    </ul>
  </section>
</main>
</body>
</html>
```